Business card for auto dealership

Looking for a clean modern design.
Would like attached logo incorporated

Industry/Entity Type

Car dealership

Contact Information for Business Card

Name, website, phone, cell, fax, email

```html
<!DOCTYPE html>
<html lang="en">
<head>
<meta charset="utf-8">
<title>Halvorsen Truck &amp; Auto Sales — Business Card</title>
<link href="https://fonts.googleapis.com/css2?family=Oswald:wght@600&family=Poppins:wght@400;500;600&display=swap" rel="stylesheet">
<style>
  :root {
    --paper: #ffffff;
    --ink: #111111;
    --card-black: #050505;
    --canvas-bg: #ffffff;
    --rule: #1a1a1a;
  }
  html, body {
    margin: 0;
    padding: 0;
    width: 1200px;
    height: 1200px;
    overflow: hidden;
    background: var(--canvas-bg);
  }
  .canvas {
    position: relative;
    width: 1200px;
    height: 1200px;
    font-family: "Poppins", sans-serif;
    color: var(--ink);
  }
  .card {
    position: absolute;
    left: 204px;
    width: 796px;
    height: 465px;
    box-sizing: border-box;
  }
  .card--front {
    top: 96px;
    background: var(--paper);
    border: 1px solid #e6e6e6;
  }
  .card--back {
    top: 638px;
    background: var(--card-black);
  }
  .front-band {
    position: absolute;
    left: 0; right: 0; bottom: 0;
    height: 20px;
    background: var(--card-black);
  }
  .person {
    position: absolute;
    left: 46px;
    top: 86px;
  }
  .person__name {
    font-family: "Oswald", sans-serif;
    font-weight: 600;
    font-size: 34px;
    letter-spacing: 1px;
    line-height: 1;
    margin: 0;
    text-transform: uppercase;
  }
  .person__role {
    font-size: 16px;
    letter-spacing: 0.8px;
    margin: 10px 0 0;
    text-transform: uppercase;
  }
  .brand {
    position: absolute;
    font-family: "Poppins", sans-serif;
    font-weight: 600;
    line-height: 1;
    text-align: right;
  }
  .brand__name { display: block; font-size: 66px; letter-spacing: -1px; }
  .brand__tag { display: block; font-size: 16px; letter-spacing: 0.6px; margin-top: 4px; text-transform: uppercase; }
  .card--front .brand { right: 48px; top: 60px; color: var(--ink); }
  .card--back .brand { left: 0; right: 0; top: 150px; text-align: center; color: var(--paper); }
  .rule {
    position: absolute;
    top: 311px;
    height: 0;
    border-top: 2px solid var(--rule);
  }
  .rule--left { left: 46px; width: 466px; }
  .rule--right { left: 529px; width: 218px; }
  .contacts {
    position: absolute;
    top: 326px;
    list-style: none;
    margin: 0;
    padding: 0;
    font-size: 18px;
    line-height: 28px;
  }
  .contacts--left { left: 46px; }
  .contacts--right { right: 48px; text-align: right; }
  .contacts li { display: flex; align-items: center; gap: 10px; }
  .contacts--right li { justify-content: flex-end; }
  .icon { width: 15px; height: 15px; fill: var(--ink); flex: none; }
  .back-web {
    position: absolute;
    left: 0; right: 0;
    top: 403px;
    text-align: center;
    color: var(--paper);
    font-size: 18px;
    letter-spacing: 0.3px;
  }
</style>
</head>
<body>
<main class="canvas">

  <section class="card card--front" aria-label="Business card front">
    <div class="person">
      <h1 class="person__name">Marcus Reed</h1>
      <p class="person__role">Managing Director</p>
    </div>

    <div class="brand">
      <span class="brand__name">Halvorsen</span>
      <span class="brand__tag">Truck &amp; Auto Sales</span>
    </div>

    <div class="rule rule--left"></div>
    <div class="rule rule--right"></div>

    <ul class="contacts contacts--left">
      <li>
        <svg class="icon" viewBox="0 0 16 16" aria-hidden="true"><path d="M3.2 1.5l2.3 2.6-1.2 1.6c.9 2 2.3 3.4 4.3 4.3l1.6-1.2 2.6 2.3-1.4 2.2C6.6 13 3 9.4 1 4.6z"/></svg>
        <span>(555) 014 2287</span>
      </li>
      <li>
        <svg class="icon" viewBox="0 0 16 16" aria-hidden="true"><path d="M4 1h8a1 1 0 0 1 1 1v12a1 1 0 0 1-1 1H4a1 1 0 0 1-1-1V2a1 1 0 0 1 1-1zm.6 1.8v9.4h6.8V2.8zM7 13.2h2v.9H7z" fill-rule="evenodd"/></svg>
        <span>(555) 014 2287</span>
      </li>
      <li>
        <svg class="icon" viewBox="0 0 16 16" aria-hidden="true"><path d="M4 1.5h8v3H4zM2 5.5h12a1 1 0 0 1 1 1v5h-2.5v-2h-9v2H1v-5a1 1 0 0 1 1-1zM4.5 10.5h7v4h-7z"/></svg>
        <span>(555) 014 2287</span>
      </li>
    </ul>

    <ul class="contacts contacts--right">
      <li>
        <span>marcus@halvorsenauto.com</span>
        <svg class="icon" viewBox="0 0 16 16" aria-hidden="true"><path d="M1 3.5h14v9H1zm1.4 1.2L8 8.6l5.6-3.9z" fill-rule="evenodd"/></svg>
      </li>
      <li>
        <span>www.halvorsenauto.com</span>
        <svg class="icon" viewBox="0 0 16 16" aria-hidden="true"><circle cx="8" cy="8" r="6.3" fill="none" stroke="#111" stroke-width="1.4"/><ellipse cx="8" cy="8" rx="2.6" ry="6.3" fill="none" stroke="#111" stroke-width="1.2"/><path d="M1.8 8h12.4M3 4.8h10M3 11.2h10" stroke="#111" stroke-width="1.1"/></svg>
      </li>
    </ul>

    <div class="front-band"></div>
  </section>

  <section class="card card--back" aria-label="Business card back">
    <div class="brand">
      <span class="brand__name">Halvorsen</span>
      <span class="brand__tag">Truck &amp; Auto Sales</span>
    </div>
    <p class="back-web">www.halvorsenauto.com</p>
  </section>

</main>
</body>
</html>
```